Business Card for a mobile physiotherapy company

I need a layout for a business card for a mobile physiotherapy company.
Slogan is "Mobile Physiotherapy - Your Road To Recovery"
Phone number is 867-402-5913
Email VantrePhysio@mailbright.ca (subject to change with website)
Website www.VantrePhysio.ca
My name and credentials: Kent Vantre Kent Vantre, BSc(kin), MPT, CAFCI, IMS
Information maybe included: Direct Billing, Services including Physiotherapy, IMS, acupuncture
Maybe include facebook and instagram logos
One side with the logo clean and sharp
Other side with details, try not to look too busy, keep everything concise

```html
<!DOCTYPE html>
<html lang="en">
<head>
<meta charset="utf-8">
<title>Vantre Physio – Business Card</title>
<link rel="stylesheet" href="https://fonts.googleapis.com/css2?family=Libre+Baskerville:wght@700&family=Open+Sans:wght@400;600&display=swap">
<style>
  :root {
    --navy: #27496f;
    --green: #12554a;
    --white: #ffffff;
    --page: #ffffff;
    --shadow: rgba(20, 30, 45, 0.22);
    --serif: "Libre Baskerville", Georgia, serif;
    --sans: "Open Sans", Arial, sans-serif;
  }
  * { box-sizing: border-box; margin: 0; padding: 0; }
  html, body { width: 1200px; height: 1200px; overflow: hidden; background: var(--page); }
  .canvas { position: relative; width: 1200px; height: 1200px; }

  .card {
    position: absolute; left: 240px; width: 720px; height: 418px;
    border-radius: 22px; overflow: hidden;
    box-shadow: 0 14px 30px var(--shadow);
  }
  .card--front { top: 142px; background: var(--navy); color: var(--white); }
  .card--back { top: 638px; background: var(--white); }

  .brand { position: absolute; left: 0; right: 0; text-align: center; font-family: var(--serif); font-weight: 700; }
  .brand__mark { display: block; margin: 0 auto; }
  .brand__name { display: block; line-height: 1; letter-spacing: 0.06em; }
  .brand__sub { display: block; line-height: 1; letter-spacing: 0.42em; padding-left: 0.42em; }

  .card--front .brand { top: 64px; color: var(--white); }
  .card--front .brand__mark { width: 60px; height: 60px; background: var(--white); margin-bottom: 40px; }
  .card--front .brand__name { font-size: 56px; }
  .card--front .brand__sub { font-size: 30px; margin-top: 10px; }

  .slogan {
    position: absolute; top: 303px; left: 0; right: 0; text-align: center;
    font-family: var(--sans); font-size: 17px; color: var(--white);
  }
  .social { position: absolute; top: 361px; left: 0; right: 0; display: flex; justify-content: center; gap: 10px; }
  .social__dot { width: 29px; height: 29px; border-radius: 50%; background: var(--white); }

  .card--back .brand { top: 28px; color: var(--navy); }
  .card--back .brand__mark { width: 48px; height: 48px; background: var(--navy); margin-bottom: 28px; }
  .card--back .brand__name { font-size: 44px; }
  .card--back .brand__sub { font-size: 23px; margin-top: 6px; }

  .person { position: absolute; top: 262px; right: 378px; text-align: right; }
  .person__name { font-family: var(--serif); font-weight: 700; font-size: 27px; color: var(--navy); letter-spacing: 0.01em; }
  .person__creds { font-family: var(--sans); font-size: 16px; color: var(--green); margin-top: 4px; letter-spacing: 0.03em; }

  .divider { position: absolute; left: 363px; top: 228px; width: 2px; height: 108px; background: var(--navy); }

  .contact { position: absolute; left: 390px; top: 243px; list-style: none; font-family: var(--sans); font-size: 17px; color: #1b1b1b; }
  .contact li { display: flex; align-items: center; height: 26px; }
  .contact svg { width: 14px; height: 14px; margin-right: 13px; fill: var(--green); flex: none; }

  .services {
    position: absolute; left: 0; right: 0; top: 365px; height: 27px;
    background: var(--green); color: var(--white);
    font-family: var(--sans); font-size: 17px; line-height: 27px; text-align: center; word-spacing: 1px;
  }
  .services .sep { margin: 0 10px; }
</style>
</head>
<body>
<main class="canvas">

  <section class="card card--front" aria-label="Card front">
    <div class="brand">
      <span class="brand__mark"></span>
      <span class="brand__name">VANTRE</span>
      <span class="brand__sub">PHYSIO</span>
    </div>
    <p class="slogan">Mobile Physiotherapy - Your Road To Recovery</p>
    <div class="social" aria-label="Social media">
      <span class="social__dot"></span>
      <span class="social__dot"></span>
    </div>
  </section>

  <section class="card card--back" aria-label="Card back">
    <div class="brand">
      <span class="brand__mark"></span>
      <span class="brand__name">VANTRE</span>
      <span class="brand__sub">PHYSIO</span>
    </div>

    <div class="person">
      <p class="person__name">KENT VANTRE</p>
      <p class="person__creds">BSc(kin), MPT, CAFCI, IMS</p>
    </div>

    <div class="divider"></div>

    <ul class="contact">
      <li>
        <svg viewBox="0 0 24 24" aria-hidden="true"><path d="M6.6 10.8a15.1 15.1 0 0 0 6.6 6.6l2.2-2.2c.3-.3.7-.4 1-.2 1.1.4 2.3.6 3.6.6.6 0 1 .4 1 1V20c0 .6-.4 1-1 1A17 17 0 0 1 3 4c0-.6.4-1 1-1h3.5c.6 0 1 .4 1 1 0 1.3.2 2.5.6 3.6.1.3 0 .7-.2 1z"/></svg>
        867-402-5913
      </li>
      <li>
        <svg viewBox="0 0 24 24" aria-hidden="true"><path d="M2 5h20v14H2z" fill="none"/><path d="M2 6v12h20V6l-10 7z"/><path d="M2 5h20l-10 7z"/></svg>
        VantrePhysio@mailbright.ca
      </li>
      <li>
        <svg viewBox="0 0 24 24" aria-hidden="true"><path d="M12 2a10 10 0 1 0 0 20 10 10 0 0 0 0-20zm6.9 6h-2.9a15 15 0 0 0-1.4-3.6A8 8 0 0 1 18.9 8zM12 4c.8 1.2 1.5 2.5 1.9 4h-3.8c.4-1.4 1.1-2.8 1.9-4zM4.3 14a8 8 0 0 1 0-4h3.4a16 16 0 0 0 0 4zm.8 2h2.9c.3 1.3.8 2.5 1.4 3.6A8 8 0 0 1 5.1 16zM8 8H5.1a8 8 0 0 1 4.3-3.6C8.8 5.5 8.3 6.7 8 8zm4 12c-.8-1.2-1.5-2.5-1.9-4h3.8c-.4 1.5-1.1 2.8-1.9 4zm2.3-6H9.7a14 14 0 0 1 0-4h4.6a14 14 0 0 1 0 4zm.3 5.6c.6-1.1 1.1-2.3 1.4-3.6h2.9a8 8 0 0 1-4.3 3.6zm1.7-5.6a16 16 0 0 0 0-4h3.4a8 8 0 0 1 0 4z"/></svg>
        www.VantrePhysio.ca
      </li>
    </ul>

    <p class="services">Direct Billing<span class="sep">|</span>Services including Physiotherapy<span class="sep">|</span>IMS<span class="sep">|</span>Acupuncture</p>
  </section>

</main>
</body>
</html>
```